inspirational business card

I want to use the Vector on Pixmarra.com (number 61827405) and I will purchase the vector to send it to the designer once the general concept is approved. You can download it for free for a one time use on providing a design for this request.
Within the vector, insert:
Denise Halvorsen
Guidance and Cooperative

I prefer a vertical card but do not require vertical.

Contact info:

Denise Halvorsen, J.D.
Collaborative Lawyer
Certified Divorce Coach
Mediation Coach
PHONE 641/382-4076
EMAIL: dhrt@quelvo.net

Website: Guidanceandcooperative.com
Settlementcourse.com

I like greens, blue and grey. I do not want black font, and would like the font to be legible without needing perfect reading vision (no super small font).
I would like the overall theme to convey growth and nurturance.
I like the vector I selected because of the growth and light portrayed.
Not too frilly or too bold. I would like to to appeal to both sexes.

Target Market(s)

Generally professional women 35-60

Industry/Entity Type

Attorney

Font styles to use
Serif
Sans Serif

Colors
acd136
cadf82
fbf289
9d9d9d

Requirements
Must have
• My project does not need to have my photo but you could use it if you want
Nice to have
• Vertical
• I like rounded edges on the cards
Should not have
• I do not like my name appearing two times in close proximity. I'm not a flowery person.

```html
<!DOCTYPE html>
<html lang="en">
<head>
<meta charset="utf-8">
<title>Denise Halvorsen — Business Card</title>
<link rel="stylesheet" href="https://fonts.googleapis.com/css2?family=Open+Sans:wght@400;600;700&family=Raleway:wght@400;500;700&display=swap">
<style>
  :root {
    --backdrop: #eeece8;
    --leaf-green: #5e9038;
    --leaf-green-deep: #4f7d2c;
    --title-green: #6a9a2f;
    --light-lime: #cadf82;
    --bright-lime: #acd136;
    --paper: #ffffff;
    --ink-grey: #6f6f6f;
    --ring-grey: #c9c9c9;
    --divider: #ececec;
  }
  * { box-sizing: border-box; margin: 0; padding: 0; }
  html, body {
    width: 1200px; height: 900px; overflow: hidden;
    background: var(--backdrop);
  }
  .canvas { position: relative; width: 1200px; height: 900px; }

  .card {
    position: absolute;
    width: 560px; height: 320px;
    border-radius: 6px;
    box-shadow: 0 10px 28px rgba(0,0,0,.16);
  }

  /* Front: green side */
  .card--front {
    left: 110px; top: 150px;
    background: var(--leaf-green);
    color: var(--paper);
    font-family: "Raleway", sans-serif;
    text-align: center;
  }
  .front-emblem {
    position: absolute; left: 50%; top: 28px;
    width: 116px; height: 116px; margin-left: -58px;
  }
  .front-name {
    position: absolute; left: 0; right: 0; top: 150px;
    font-size: 44px; font-weight: 400; letter-spacing: .5px;
  }
  .front-tagline {
    position: absolute; left: 0; right: 0; top: 206px;
    font-size: 25px; font-weight: 400;
  }
  .front-web {
    position: absolute; left: 0; right: 0; top: 256px;
    font-family: "Open Sans", sans-serif;
    font-size: 15px; font-weight: 600;
  }

  /* Back: white contact side */
  .card--back {
    left: 530px; top: 420px;
    background: var(--paper);
    font-family: "Open Sans", sans-serif;
  }
  .back-emblem {
    position: absolute; left: 60px; top: 55px;
    width: 210px; height: 210px;
  }
  .back-divider {
    position: absolute; left: 315px; top: 30px; bottom: 30px;
    width: 1px; background: var(--divider);
  }
  .contact {
    position: absolute; left: 340px; top: 78px;
  }
  .contact-name {
    color: var(--title-green);
    font-size: 17px; font-weight: 700; letter-spacing: .3px;
    text-transform: uppercase;
  }
  .contact-role {
    color: var(--ink-grey);
    font-size: 14px; line-height: 21px; margin-left: 12px;
  }
  .contact-role:first-of-type { margin-top: 4px; }
  .contact-lines { margin-top: 16px; margin-left: 12px; }
  .contact-line {
    display: flex; align-items: center; gap: 8px;
    color: var(--ink-grey); font-size: 14px; line-height: 21px;
  }
  .contact-line svg { width: 12px; height: 12px; fill: var(--title-green); }
</style>
</head>
<body>
<main class="canvas">

  <section class="card card--front" aria-label="Business card front">
    <svg class="front-emblem" viewBox="0 0 116 116" role="img" aria-label="Tree of growth illustration in a circle">
      <circle cx="58" cy="58" r="55" fill="none" stroke="#ffffff" stroke-width="4"/>
      <circle cx="58" cy="54" r="46" fill="#ffffff" opacity=".85"/>
    </svg>
    <h1 class="front-name">Denise Halvorsen</h1>
    <p class="front-tagline">Guidance and Cooperative</p>
    <p class="front-web">www.Guidanceandcooperative.com</p>
  </section>

  <section class="card card--back" aria-label="Business card back">
    <svg class="back-emblem" viewBox="0 0 210 210" role="img" aria-label="Green tree illustration with grey ring">
      <defs>
        <radialGradient id="leafGlow" cx="50%" cy="35%" r="65%">
          <stop offset="0%" stop-color="#cadf82"/>
          <stop offset="60%" stop-color="#acd136"/>
          <stop offset="100%" stop-color="#6a9a2f"/>
        </radialGradient>
      </defs>
      <circle cx="105" cy="110" r="98" fill="#d4d4d4"/>
      <circle cx="105" cy="103" r="94" fill="#ffffff"/>
      <circle cx="105" cy="100" r="82" fill="url(#leafGlow)"/>
    </svg>

    <div class="back-divider"></div>

    <div class="contact">
      <h2 class="contact-name">Denise Halvorsen, J.D.</h2>
      <p class="contact-role">Collaborative Lawyer</p>
      <p class="contact-role">Certified Divorce Coach</p>
      <div class="contact-lines">
        <p class="contact-line">
          <svg viewBox="0 0 24 24" aria-hidden="true"><path d="M6.6 10.8a15.1 15.1 0 0 0 6.6 6.6l2.2-2.2a1 1 0 0 1 1-.25 11.4 11.4 0 0 0 3.6.57 1 1 0 0 1 1 1V20a1 1 0 0 1-1 1A17 17 0 0 1 3 4a1 1 0 0 1 1-1h3.5a1 1 0 0 1 1 1c0 1.25.2 2.45.57 3.57a1 1 0 0 1-.25 1z"/></svg>
          641/382-4076
        </p>
        <p class="contact-line">
          <svg viewBox="0 0 24 24" aria-hidden="true"><path d="M2 5h20v14H2z M3.5 6.5 12 13l8.5-6.5" stroke="#ffffff" stroke-width="1.6"/></svg>
          dhrt@quelvo.net
        </p>
      </div>
    </div>
  </section>

</main>
</body>
</html>
```